Refresh of The Marwick Partners business card

Update business card design using existing primary logo. Names, numbers, etc. are too hard to read on current design.

Target Market(s)

We are a CPA firm.

Industry/Entity Type

Accountant

Contact Information for Business Card

update current card

Colors
0355a3
3176b5
85acd3
0792cd

Requirements
Must have
• Easier to read phone numbers and names
• Use existing logo
Nice to have
• We love our color scheme and current TMP logo. But the names and phone numbers are too small and card just look old and stale.

```html
<!DOCTYPE html>
<html lang="en">
<head>
<meta charset="utf-8">
<title>The Marwick Partners – Business Card</title>
<link rel="stylesheet" href="https://fonts.googleapis.com/css2?family=Montserrat:wght@400;500;600&family=Tinos&display=swap">
<style>
  :root {
    --navy: #1f3366;
    --navy-text: #1f3a7a;
    --ink: #2a2f3a;
    --grey-swoosh: #4a4c52;
    --paper: #ffffff;
    --backdrop: #ebe8e3;
    --shadow: rgba(0, 0, 0, 0.28);
  }
  * { margin: 0; padding: 0; box-sizing: border-box; }
  html, body { width: 1200px; height: 1000px; overflow: hidden; }
  body {
    background: var(--backdrop);
    font-family: "Montserrat", Arial, sans-serif;
    position: relative;
  }
  .card {
    position: absolute;
    left: 295px;
    width: 586px;
    height: 333px;
    overflow: hidden;
    box-shadow: 0 6px 14px var(--shadow);
  }
  .card--front { top: 150px; background: var(--paper); }
  .card--back { top: 517px; background: var(--navy); }

  .wave { position: absolute; left: 0; top: 0; width: 586px; height: 333px; }

  .brand { position: absolute; display: flex; align-items: center; }
  .brand__dot { border-radius: 50%; flex: none; }
  .brand__name {
    font-weight: 600;
    letter-spacing: 1.5px;
    line-height: 1.15;
    text-transform: uppercase;
  }
  .card--front .brand { left: 45px; top: 34px; gap: 14px; }
  .card--front .brand__dot { width: 64px; height: 64px; background: var(--navy); }
  .card--front .brand__name { color: var(--navy-text); font-size: 18px; }

  .card--back .brand { left: 131px; top: 119px; gap: 26px; }
  .card--back .brand__dot { width: 96px; height: 96px; border: 3px solid var(--paper); }
  .card--back .brand__name { color: var(--paper); font-size: 26px; }

  .person { position: absolute; left: 47px; top: 162px; }
  .person__name {
    font-family: "Tinos", "Times New Roman", serif;
    font-size: 20px;
    color: var(--navy-text);
    letter-spacing: 0.3px;
  }
  .person__role { font-size: 16px; color: var(--ink); margin-top: 1px; }

  .contacts { position: absolute; left: 326px; top: 164px; list-style: none; }
  .contacts li {
    display: flex; align-items: center; gap: 11px;
    font-size: 14px; color: var(--ink); height: 18.7px; letter-spacing: 0.3px;
  }
  .contacts svg { width: 13px; height: 13px; fill: var(--navy); flex: none; }

  .address { position: absolute; left: 46px; top: 266px; color: var(--paper); font-size: 14px; line-height: 19px; letter-spacing: 0.3px; }
  .address svg { width: 11px; height: 14px; fill: var(--paper); display: block; margin: 0 0 6px 0; }

  .website {
    position: absolute; left: 0; right: 0; top: 285px; text-align: center;
    color: var(--paper); font-size: 14px; letter-spacing: 0.8px;
  }
</style>
</head>
<body>
  <section class="card card--front" aria-label="Business card front">
    <svg class="wave" viewBox="0 0 586 333" aria-hidden="true">
      <path d="M0 226 C 170 250 330 290 560 283 C 420 292 240 270 0 240 Z" fill="var(--grey-swoosh)"/>
      <path d="M0 246 C 180 272 360 302 586 276 L586 333 L0 333 Z" fill="var(--navy)"/>
    </svg>
    <div class="brand">
      <span class="brand__dot"></span>
      <span class="brand__name">The Marwick<br>Partners</span>
    </div>
    <div class="person">
      <div class="person__name">DANIEL R. MARWICK, CPA</div>
      <div class="person__role">Founder</div>
    </div>
    <ul class="contacts">
      <li><svg viewBox="0 0 24 24"><path d="M6.6 10.8a15.1 15.1 0 0 0 6.6 6.6l2.2-2.2c.3-.3.7-.4 1-.2 1.1.4 2.3.6 3.6.6.6 0 1 .4 1 1V20c0 .6-.4 1-1 1A17 17 0 0 1 3 4c0-.6.4-1 1-1h3.5c.6 0 1 .4 1 1 0 1.3.2 2.5.6 3.6.1.3 0 .7-.2 1z"/></svg>555.210.4837</li>
      <li><svg viewBox="0 0 24 24"><path d="M7 1h10a2 2 0 0 1 2 2v18a2 2 0 0 1-2 2H7a2 2 0 0 1-2-2V3a2 2 0 0 1 2-2zm0 3v14h10V4zm5 15.5a1.2 1.2 0 1 0 0 2.4 1.2 1.2 0 0 0 0-2.4z"/></svg>555.382.1906</li>
      <li><svg viewBox="0 0 24 24"><path d="M6 2h12v5H6zM4 8h16a2 2 0 0 1 2 2v7h-4v5H6v-5H2v-7a2 2 0 0 1 2-2zm4 7v5h8v-5z"/></svg>555.647.2210</li>
      <li><svg viewBox="0 0 24 24"><path d="M2 5h20v2l-10 6L2 7zm0 4.3 10 6 10-6V19H2z"/></svg>dan@marwickpartners.com</li>
    </ul>
    <div class="address">
      <svg viewBox="0 0 12 16"><path d="M6 0a6 6 0 0 0-6 6c0 4.5 6 10 6 10s6-5.5 6-10a6 6 0 0 0-6-6zm0 8.3A2.3 2.3 0 1 1 6 3.7a2.3 2.3 0 0 1 0 4.6z"/></svg>
      218 Linden Ave.<br>Suite 310 Harbor City, Florida 32000
    </div>
  </section>

  <section class="card card--back" aria-label="Business card back">
    <div class="brand">
      <span class="brand__dot"></span>
      <span class="brand__name">The Marwick<br>Partners</span>
    </div>
    <div class="website">www.marwickpartners.com</div>
  </section>
</body>
</html>
```